Pitch deck for fundraising for a timber drying business

We have the basic content in a powerpoint but need someone to take that and make an attractive and engaging document for a reader who may see hundreds of these a week so visual impact is key.
We are launching a timber drying business in Australia using an exclusive line of kilns not otherwise available in Australia.
Designs should focus on natural tones and connections with forests and timber, probably with a green (colour) focus.
Updates

Sick

Target Market(s)

investors, wealthyindividuals

Colors

Designer to choose colors to be used in the design.

Requirements
Nice to have
• Design in Canva or similar

```html
<!DOCTYPE html>
<html lang="en">
<head>
<meta charset="utf-8">
<title>Kilnwood Partners Pitch Deck</title>
<link href="https://fonts.googleapis.com/css2?family=Poppins:wght@300;400;500;600;700&display=swap" rel="stylesheet">
<style>
:root{
  --canvas:#c6c6c6;
  --paper:#ffffff;
  --ink:#4a4a4a;
  --title:#1f4a17;
  --bright:#0bb14b;
  --mint:#e3f0dc;
  --mint-soft:#eef6ea;
  --panel:#f3f3f3;
  --forest:#3f6130;
  --forest-deep:#2c4a22;
  --olive:#4f8a33;
}
*{margin:0;padding:0;box-sizing:border-box}
html,body{width:1200px;height:2400px;overflow:hidden}
body{background:var(--canvas);font-family:'Poppins',sans-serif;color:var(--ink);position:relative}
.slide{position:absolute;width:518px;height:291px;background:var(--paper);overflow:hidden;box-shadow:6px 10px 18px rgba(0,0,0,.22);border-bottom:2px solid var(--bright)}
.abs{position:absolute}
.slide-title{position:absolute;left:0;right:0;top:16px;text-align:center;color:var(--title);font-weight:700;font-size:19px;letter-spacing:.2px}
.ornament{position:absolute;left:50%;transform:translateX(-50%);top:44px;width:40px;height:6px}
.photo{position:absolute}
.small{font-size:6px;line-height:1.35}
.tiny{font-size:4.6px;line-height:1.4}
.hl{color:var(--bright);font-weight:600}
ul.bullets{list-style:none}
ul.bullets li{position:relative;padding-left:12px;margin-bottom:6px}
ul.bullets li::before{content:"";position:absolute;left:2px;top:3px;width:4px;height:4px;border:1px solid var(--bright);transform:rotate(45deg)}
/* title slide */
.cover-panel{left:249px;top:16px;width:247px;height:257px;background:var(--mint);text-align:center}
.cover-panel h1{margin-top:96px;color:var(--title);font-size:19px;line-height:1.25;font-weight:700}
.cover-panel .date{font-size:12px;color:#555;margin-top:14px}
.accent-bar{background:var(--bright)}
/* business model */
.step{position:absolute;top:99px;width:99px}
.step .pic{height:68px;border:3px solid #fff}
.step .box{margin-top:12px;border:1px dashed rgba(255,255,255,.7);height:45px;text-align:center;color:#e6efe0;font-size:7.5px;padding-top:5px;line-height:1.2}
.step .box b{display:block;color:#fff;font-size:10.5px;margin-top:6px;font-weight:600}
/* tables */
table{border-collapse:collapse;width:100%}
.risk-table th{color:#fff;font-size:9px;font-weight:600;height:20px}
.risk-table th.k{background:var(--olive)}
.risk-table th.v{background:var(--bright)}
.risk-table td{font-size:4.6px;line-height:1.4;padding:4px 6px;vertical-align:middle;border-bottom:1px solid #fff}
.risk-table td.k{background:var(--panel);width:35%;font-size:5.2px}
.risk-table tr:nth-child(even) td{background:var(--mint-soft)}
.fin-table th{background:var(--forest-deep);color:#fff;font-size:7px;height:13px;font-weight:600}
.fin-table td{font-size:5px;font-weight:600;color:var(--title);height:13px;padding-left:7px;border-right:1px solid #fff}
.fin-table tr:nth-child(odd) td{background:var(--mint-soft)}
.fin-table tr:nth-child(even) td{background:#f7f7f7}
/* cards */
.plan-card{position:absolute;top:97px;width:145px;height:170px;background:#f1f1f1;text-align:center;padding-top:38px}
.plan-card h3{color:var(--bright);font-size:7.5px;font-weight:600;margin-bottom:8px}
.plan-card ul{text-align:left;padding:0 9px}
.plan-card li{margin-bottom:4px}
.plan-dot{position:absolute;top:65px;width:57px;height:57px;border-radius:50%;border:3px solid #fff;box-shadow:0 2px 4px rgba(0,0,0,.25)}
.member{position:absolute;width:137px;height:110px;background:#fff;box-shadow:0 2px 8px rgba(0,0,0,.18);padding:10px}
.member .face{position:absolute;left:10px;top:10px;width:38px;height:38px;border-radius:50%;background:linear-gradient(#9a9a9a,#5f5f5f)}
.member .name{position:absolute;left:56px;top:18px;color:var(--bright);font-size:8px;font-weight:600}
.member .role{position:absolute;left:56px;top:30px;font-size:5.5px;font-style:italic;color:#777}
.member p{position:absolute;left:10px;right:12px;top:60px;font-size:6.5px;line-height:1.35}
.forest-band{background:linear-gradient(180deg,#4d6e3a,#34522a 60%,#2a4420)}
.dark-text{color:#e8efe2}
.dark-text h4{font-size:5px;color:#fff;font-weight:600;margin-bottom:2px}
.dark-text p{font-size:4.4px;line-height:1.4;margin-bottom:6px}
</style>
</head>
<body>

<svg width="0" height="0" style="position:absolute">
  <defs>
    <symbol id="orn" viewBox="0 0 40 6"><line x1="0" y1="3" x2="15" y2="3" stroke="#9ac88c" stroke-width=".8"/><circle cx="20" cy="3" r="2.2" fill="none" stroke="#9ac88c" stroke-width=".8"/><line x1="25" y1="3" x2="40" y2="3" stroke="#9ac88c" stroke-width=".8"/></symbol>
  </defs>
</svg>

<!-- Cover -->
<section class="slide cover" style="left:63px;top:236px">
  <div class="photo" role="img" aria-label="Looking up into a green forest canopy" style="left:19px;top:16px;width:222px;height:257px;background:radial-gradient(circle at 50% 45%,#e6f2d4,#7fb24a 35%,#3a6a22 70%,#233a16)"></div>
  <div class="abs cover-panel">
    <h1>KILNWOOD PARTNERS<br>PITCH DECK</h1>
    <svg style="display:block;margin:8px auto 0" width="40" height="6"><use href="#orn"/></svg>
    <div class="date">August 11, 2020</div>
  </div>
  <div class="abs accent-bar" style="left:496px;top:16px;width:22px;height:257px"></div>
</section>

<!-- Introduction -->
<section class="slide intro" style="left:620px;top:411px">
  <h2 class="slide-title">Introduction</h2>
  <svg class="ornament"><use href="#orn"/></svg>
  <div class="abs" style="left:19px;top:64px;width:480px;height:215px;background:#f5f6f4"></div>
  <div class="abs" role="img" aria-label="Silhouette of a pine forest edge" style="left:0;top:200px;width:518px;height:91px;background:linear-gradient(180deg,rgba(245,246,244,0),#8ea88a 45%,#2f4b2a)"></div>
  <div class="abs small" style="left:40px;top:82px;width:190px">
    <p style="margin-bottom:8px">Kilnwood Partners (KWP) has secured exclusive access to a superior timber drying technology (AirCure kilns) that has been in commercial production since 1980.</p>
    <p style="margin-bottom:8px">KWP will leverage this technology to build a hardwood drying business, initially focused on the stair tread market in Sydney and Brisbane.</p>
    <p style="margin-bottom:8px">Hardwood stair tread timber has an approximate gross margin of <span class="hl">$XXXX/m3 (XX%).</span></p>
    <p>KWP will sell directly to stair tread installers enabling us to retain the bulk of the gross margin as net profit.</p>
  </div>
  <div class="abs small" style="left:280px;top:82px;width:200px">
    <p style="margin-bottom:8px">AirCure kilns are relatively inexpensive <span class="hl">($US79–205K)</span>, modular in design, and return approximately <span class="hl">300%</span> per annum. As a result, KWP will be able to scale without additional equity or debt funding.</p>
    <p style="margin-bottom:8px">The Australian hardwood industry is worth around <span class="hl">$7bn</span> pa on <span class="hl">700,000m3</span> of sawn timber but <span class="hl">93%</span> of logs are exported. With 10 kilns KWP would dry less than 1% of all sawn timber but turn over <span class="hl">$XXm</span> and nett <span class="hl">$XXm</span> with huge growth potential from value adding exported logs.</p>
    <p>This is not a tech play but a cash cow investment to be held long term. We have a simple business model, using established technology to disrupt a technologically stagnant, but growing industry.</p>
  </div>
</section>

<!-- Business Model -->
<section class="slide model" style="left:63px;top:596px">
  <h2 class="slide-title">Business Model</h2>
  <svg class="ornament"><use href="#orn"/></svg>
  <p class="abs" style="left:50px;right:50px;top:63px;text-align:center;font-size:9px;line-height:1.3;color:#333">We are using established technology to disrupt the existing timber supply chain with a simple <b>4 step</b> business model</p>
  <div class="abs forest-band" role="img" aria-label="Forest floor backdrop" style="left:0;top:136px;width:518px;height:109px"></div>
  <div class="step" style="left:30px"><div class="pic" role="img" aria-label="Stack of cut hardwood boards" style="background:linear-gradient(135deg,#a0623e,#5c3521)"></div><div class="box">Buy cut timber<br>from sawmills<b>$XXX m3</b></div></div>
  <div class="step" style="left:150px"><div class="pic" role="img" aria-label="Timber stacked inside a drying kiln" style="background:linear-gradient(135deg,#d8cab4,#8a6a48)"></div><div class="box">Dry it in our<br>kilns<b>$XXXm3</b></div></div>
  <div class="step" style="left:270px"><div class="pic" role="img" aria-label="Dressing machine processing timber" style="background:linear-gradient(135deg,#c9d0d6,#6d5540)"></div><div class="box">Dress and<br>deliver<b>$XXX m3</b></div></div>
  <div class="step" style="left:390px"><div class="pic" role="img" aria-label="Finished hardwood stair tread" style="background:radial-gradient(ellipse at 50% 55%,#6a3a22 0 30%,#e3f0dc 32%)"></div><div class="box">Sell dried stair<br>treads to installers<b>$XXXm3</b></div></div>
  <p class="abs" style="left:0;right:0;top:256px;text-align:center;font-size:13px;color:#444"><span class="hl" style="font-weight:700">~ $XXXm3</span> Net profit</p>
</section>

<!-- Market Overview -->
<section class="slide market" style="left:620px;top:771px">
  <div class="abs" style="left:0;top:0;width:518px;height:40px;background:#f3f3f3"></div>
  <h2 class="slide-title">Market Overview</h2>
  <svg class="ornament"><use href="#orn"/></svg>
  <ul class="abs bullets tiny" style="left:20px;top:76px;width:272px">
    <li>The total value of the Australian timber market is <b>$23.9bn*</b> with hardwood accounting for over <b>$7bn</b> and softwood the balance. The hardwood market has been growing strongly, posting 10% growth in volume of logs harvested and a 13% increase in price in 2017 despite a 5% fall in housing construction.</li>
    <li>The hardwood industry however is massively under developed with <b>93%*</b> of all plantation hardwood logs being exported – with no value adding.</li>
    <li>The total volume of sawn hardwood timber in 2018 was 700,000m3. With just 10 kilns we would dry less than 6,800m3 pa, gross <b>$30.6m</b> in revenue and net <b>$18.5m</b> with significant opportunity to expand.</li>
    <li>In NSW logs are sourced through either Regional Forests Agency (Reid knows and has worked with the Chair previously) on either a quota or spot price basis or through the logging of private forests. KWP will commence by sourcing timber from private forests as there are numerous landholders and concert loggers to ensure timber supply and mitigate sourcing risk.</li>
    <li>To quantify the direct addressable market KWP conducted extensive market research, contacting 98 stair installers, joineries and furniture manufacturers in addition to wholesalers. Stair installers pay between $XXX and $XXXm3 with an average of just over $XX00m3 whereas wholesalers buy at around <b>$XX00m3</b>.</li>
    <li>Include Owen's timber data on stair tread market</li>
  </ul>
  <div class="abs" style="left:342px;top:62px;width:150px;height:202px;border:8px solid var(--bright)"></div>
  <div class="photo" role="img" aria-label="Mountain pine forest at dusk" style="left:312px;top:89px;width:149px;height:178px;background:linear-gradient(180deg,#d9c6a4,#8a8f7a 35%,#2f4a2c 65%,#5e5c52)"></div>
</section>

<!-- Post Drying -->
<section class="slide post" style="left:63px;top:956px">
  <h2 class="slide-title">Post Drying Process</h2>
  <svg class="ornament"><use href="#orn"/></svg>
  <div class="abs" style="left:0;top:78px;width:208px;height:179px;background:#f3f3f3"></div>
  <ul class="abs bullets" style="left:18px;top:92px;width:180px;font-size:7.3px;line-height:1.3">
    <li>Dried stair treads are either delivered skip dressed or sized and finished with volumes being around 50:50 of each. We will commence by offering a skip dressed product as it is the simplest to produce.</li>
    <li>Skip dressing involves running the dried timber through a thicknesser or moulder to roughly level two sides of timber and expose the grain. This allows the quality of the timber grade (Select, Standard or feature) to be assessed.</li>
    <li>Once dressed, the timber is palletised ready for delivery to the client.</li>
  </ul>
  <div class="photo" role="img" aria-label="Timber passing through a thicknesser machine" style="left:214px;top:78px;width:271px;height:179px;background:linear-gradient(160deg,#3b342c,#8a7a62 45%,#d7cdb8 60%,#4a3c2e)"></div>
  <div class="abs" style="left:226px;top:90px;width:247px;height:155px;border:1px solid rgba(255,255,255,.8)"></div>
  <div class="abs accent-bar" style="left:490px;top:78px;width:28px;height:179px"></div>
</section>

<!-- Business Plan -->
<section class="slide plan" style="left:620px;top:1131px">
  <h2 class="slide-title">Business Plan</h2>
  <svg class="ornament"><use href="#orn"/></svg>
  <div class="abs forest-band" role="img" aria-label="Misty forest backdrop" style="left:0;top:178px;width:518px;height:113px;background:linear-gradient(180deg,#8da07e,#4a6a3a 60%,#34502a)"></div>
  <div class="plan-card tiny" style="left:30px"><h3>Establishment</h3><ul class="bullets"><li>Rent 300m2+ warehouse space in Coffs Harbour – central to north coast hardwood forests. A site will be selected once an ETA for the initial kiln is established. Initial lease term 6 months with options for further terms of 2 years.</li><li>An example: 747m2 factory and hardstand in Coffs Harbour $36,000pa</li><li>We are also in preliminary discussions to lease a small sawmill as an alternative.</li></ul></div>
  <div class="plan-card tiny" style="left:186px"><h3>AirCure trial</h3><ul class="bullets"><li>In order to minimise risk and reduce lead time (6 v 14 weeks) on the first machine we will order an AirCure Plus ($US79K) to undertake initial production.</li><li>We will have conducted 2 production runs within the first month and will then decide whether to order an AirCure Turbo (up to 14 week lead time) or undertake further testing.</li></ul></div>
  <div class="plan-card tiny" style="left:343px"><h3>Scaling production</h3><ul class="bullets"><li>Following the successful trial of the AirCure Plus we will purchase an AirCure Turbo as it has 380% greater throughput (being 50% larger and twice as fast to dry). Whilst more expensive, Turbos minimise the amount of labour in loading and reduce the floor space required for a given level of output.</li><li>We propose to acquire all future equipment debt free and it is likely that our growth will only be constrained by the availability of AirCure Turbos and the seasonal availability of timber.</li></ul></div>
  <div class="plan-dot" role="img" aria-label="Empty warehouse interior" style="left:74px;background:linear-gradient(#c9c3b8,#6b645a)"></div>
  <div class="plan-dot" role="img" aria-label="Drying kiln unit" style="left:230px;background:linear-gradient(#6f8fb0,#7a3b2a)"></div>
  <div class="plan-dot" role="img" aria-label="Large production floor" style="left:387px;background:linear-gradient(#dcd8cf,#8c8574)"></div>
  <p class="abs" style="left:0;right:0;top:278px;text-align:center;font-size:4px;color:#e8efe2">*Example listing: warehouse and hardstand for lease, Coffs Harbour NSW 2450</p>
</section>

<!-- Financials -->
<section class="slide financials" style="left:63px;top:1317px">
  <h2 class="slide-title">Financials</h2>
  <svg class="ornament"><use href="#orn"/></svg>
  <svg class="abs" style="left:26px;top:66px" width="270" height="128" viewBox="0 0 270 128" font-family="Poppins,sans-serif" font-size="4.5" fill="#555">
    <g stroke="#e2e2e2" stroke-width=".5">
      <line x1="36" y1="6" x2="230" y2="6"/><line x1="36" y1="24" x2="230" y2="24"/><line x1="36" y1="42" x2="230" y2="42"/><line x1="36" y1="60" x2="230" y2="60"/><line x1="36" y1="78" x2="230" y2="78"/><line x1="36" y1="96" x2="230" y2="96"/><line x1="36" y1="114" x2="230" y2="114"/>
    </g>
    <text x="2" y="8">$30,000,000</text><text x="2" y="26">$25,000,000</text><text x="2" y="44">$20,000,000</text><text x="2" y="62">$15,000,000</text><text x="2" y="80">$10,000,000</text><text x="4" y="98">$5,000,000</text><text x="24" y="116">$0</text>
    <rect x="52" y="104" width="13" height="10" fill="#a6d58f"/><rect x="68" y="107" width="13" height="7" fill="#0bb14b"/>
    <rect x="112" y="57" width="13" height="57" fill="#a6d58f"/><rect x="128" y="82" width="13" height="32" fill="#0bb14b"/>
    <rect x="172" y="17" width="13" height="97" fill="#a6d58f"/><rect x="188" y="60" width="13" height="54" fill="#0bb14b"/>
    <text x="58" y="124">Year 1</text><text x="118" y="124">Year 2</text><text x="178" y="124">Year 3</text>
    <rect x="236" y="55" width="4" height="4" fill="#a6d58f"/><text x="242" y="59">Revenue</text>
    <rect x="236" y="67" width="4" height="4" fill="#0bb14b"/><text x="242" y="71">EBITDA</text>
  </svg>
  <table class="fin-table abs" style="left:25px;top:202px;width:268px">
    <tr><th></th><th>Year 1</th><th>Year 2</th><th>Year 3</th></tr>
    <tr><td>EBITDA</td><td></td><td></td><td></td></tr>
    <tr><td>Cumulative cash</td><td></td><td></td><td></td></tr>
    <tr><td>No. kilns</td><td></td><td></td><td></td></tr>
    <tr><td>Monthly Recurring Profit</td><td></td><td></td><td></td></tr>
  </table>
  <div class="abs small" style="left:319px;top:69px;width:173px;height:201px;background:#f3f3f3;padding:13px 15px;font-size:6.4px">
    <p style="margin-bottom:6px">Kilnwood Partners will offer investors high levels of cash returns with the business netting around <span class="hl">$XXX</span> pm with just the AirCure Plus and almost $XXX pm with a Plus and a Turbo in month 7.</p>
    <p style="margin-bottom:6px">From there we will ramp up production capacity in accordance with sales and AirCure production capacity.</p>
    <p style="margin-bottom:6px">We view KWP as a long term hold, paying out <span class="hl">80%+</span> of net profit where there aren't opportunities to grow the business.</p>
    <p>By the time we have 10 total kilns (end of year 3) we expect to be distributing a total of approximately <span class="hl">$XX</span> per month and retaining <span class="hl">$XXX</span> pm.</p>
  </div>
</section>

<!-- Risk (table) -->
<section class="slide risk-main" style="left:620px;top:1491px">
  <div class="photo" role="img" aria-label="Sunlit forest trees" style="left:363px;top:0;width:155px;height:291px;background:linear-gradient(160deg,#b9c96a,#5f7e2e 40%,#3c5a24 75%,#6d5a32)"></div>
  <h2 class="slide-title" style="right:155px">Risk</h2>
  <svg class="ornament" style="left:258px"><use href="#orn"/></svg>
  <table class="risk-table abs" style="left:34px;top:66px;width:452px;background:#fff">
    <tr><th class="k">Risk</th><th class="v">Mitigation</th></tr>
    <tr><td class="k">Disruption to log supply</td><td>Coffs Harbour is central to the hardwood timber forests of the north coast, allowing KWP to economically draw timber from a wider geographic area reducing the potential for localised issues such as weather or fires to impact supply.</td></tr>
    <tr><td class="k">Unable to obtain boards from sawmills</td><td>Diversify supply of boards, contract with state and private forests for own supply of logs and use contract sawmilling. Phase 3 develop own sawmilling capacity.</td></tr>
    <tr><td class="k">Timber boards not to specification</td><td>Inspect and test delivered timber pre-drying to allow rejection of out of specification boards. Inspect post-drying boards to ensure they meet specification. Consider independent testing as part of out-bound QA process.</td></tr>
    <tr><td class="k">Kiln doesn't perform to expectations</td><td>Warranty and product support for a fault. If operation of machine does not achieve expected levels of output increase number of machines or air-dry timber before placement in kiln to reduce kiln times.</td></tr>
    <tr><td class="k">Ability to supply required species timber</td><td>We will initially only dry loads of the most commonly used timber – blackbutt. As capacity and confidence in quality improve we will start to broaden the range of species we dry, this will also help mitigate any risks around supply of timber.</td></tr>
    <tr><td class="k">Copycat competitor</td><td>Our exclusive agreement for the supply of AirCure equipment excludes direct competition in the short term but there are alternative kilns but with lesser performance. Phase 2 of the strategic plan is focussed on developing a highly connected and integrated sales channel with the market in order to create a barrier to entry.</td></tr>
  </table>
</section>

<!-- Risk (general) -->
<section class="slide risk-extra" style="left:63px;top:1677px">
  <h2 class="slide-title">Risk</h2>
  <svg class="ornament"><use href="#orn"/></svg>
  <table class="risk-table abs" style="left:33px;top:61px;width:452px">
    <tr><th class="k">Risk</th><th class="v">Mitigation</th></tr>
    <tr><td class="k" style="height:44px">Competitor response</td><td>In the short term competitors are unable to compete on drying time or quality and will only have price as an option. KWP has very low fixed costs and the lowest marginal costs of any competitor enabling us to match or better any pricing moves by a competitor. Given the size of the market, however, we believe we would need to expand beyond 3 kilns before competitors became aware of our activities and that would provide a substantial financial base to address any competitive challenges.</td></tr>
  </table>
  <div class="abs forest-band" role="img" aria-label="Dense forest backdrop" style="left:0;top:144px;width:518px;height:145px"></div>
  <div class="abs dark-text" style="left:37px;top:155px;width:210px">
    <h4>Business Model Risk</h4><p>The certainty and timing of KWP's sales is a primary factor driving the year one financial performance of the Company. Equally, timber and AirCure kiln availability may adversely affect performance.</p>
    <h4>Strategic Risk</h4><p>Operating within a specific industry and within a particular time frame gives rise to a number of risks outside the control of the Company. A shift in the desires of customers as an outcome of market movements or government policy could have adverse effects on the company.</p>
    <h4>Insolvency Risk</h4><p>The Company is an unlisted business and while the Directors believe the financial projections including the funding requirements are reasonable there can be no guarantee they will be achieved or that the funding will be sufficient.</p>
  </div>
  <div class="abs dark-text" style="left:271px;top:155px;width:210px">
    <h4>Regulatory Risk</h4><p>Political, taxation, economic, legislative or regulatory change may have an adverse effect on the Company's operations. Government action or policy change may adversely affect the Company's operations and financial performance.</p>
    <h4>Liquidity Risk</h4><p>At this point the shares in the Company are an unlisted illiquid stock and therefore there is no open market for them. There can be no guarantee that the Company will achieve its stated objectives or that any forward-looking statements will eventuate. Accordingly, an investment in the Company should be regarded as speculative. This information does not purport to be a comprehensive statement of all risks, an investor should seek and obtain professional advice prior to deciding whether or not to invest in Kilnwood Partners.</p>
  </div>
</section>

<!-- Our Team -->
<section class="slide team" style="left:620px;top:1852px">
  <div class="abs" role="img" aria-label="Green forest path" style="left:0;top:0;width:252px;height:291px;background:linear-gradient(160deg,#86a05a,#4c6b32 45%,#2f4a22)"></div>
  <div class="member" style="left:26px;top:33px"><div class="face" role="img" aria-label="Team member portrait"></div><div class="name">Name here</div><div class="role">Subtitle here</div><p>Lorem Ipsum is simply dummy text of the printing. Lorem Ipsum has been the industry's standard dummy text</p></div>
  <div class="member" style="left:177px;top:33px"><div class="face" role="img" aria-label="Team member portrait"></div><div class="name">Name here</div><div class="role">Subtitle here</div><p>Lorem Ipsum is simply dummy text of the printing. Lorem Ipsum has been the industry's standard dummy text</p></div>
  <div class="member" style="left:26px;top:156px"><div class="face" role="img" aria-label="Team member portrait"></div><div class="name">Name here</div><div class="role">Subtitle here</div><p>Lorem Ipsum is simply dummy text of the printing. Lorem Ipsum has been the industry's standard dummy text</p></div>
  <div class="member" style="left:177px;top:156px"><div class="face" role="img" aria-label="Team member portrait"></div><div class="name">Name here</div><div class="role">Subtitle here</div><p>Lorem Ipsum is simply dummy text of the printing. Lorem Ipsum has been the industry's standard dummy text</p></div>
  <h2 class="abs" style="left:360px;width:124px;top:92px;text-align:center;color:var(--title);font-size:19px;font-weight:700">Our Team</h2>
  <svg class="abs" style="left:402px;top:122px" width="40" height="6"><use href="#orn"/></svg>
  <div class="abs small" style="left:361px;top:140px;width:124px;font-size:5.4px;text-align:justify">
    <p style="margin-bottom:6px">Lorem Ipsum is simply dummy text of the printing and typesetting industry. Lorem Ipsum has been the industry's standard dummy text ever since the 1500s, when an unknown printer took a galley of type and scrambled it to make a type specimen book.</p>
    <p>It has survived not only five centuries, but also the leap into electronic typesetting, remaining essentially unchanged.</p>
  </div>
</section>

</body>
</html>
```